Business Card Design Project

We have a logo, but would like to expand the use of it into a business card design. We are a B2B technology exchange platform for institutional investors to invest excess cash into short term assets matching their credit and pricing parameters. The assets are fractionalized and investors invest in portions.

Our customers are large, institutional, financial companies who are a bit traditional. We are high energy rebels with a cause...we are a disruptive technology and want to be viewed as a game changer but we need to present an image of trustworthiness and secure.

We are open not only to the image design but the material, die cut, etc. but want to stay in the traditional size of a business card.

We have other formats of the logo if needed. Our website is www.brambleharbor.com

I have posted a powerpoint template that we have been using.  This should not be considered the template we will use (after business cards we will have another project to incorporate business card design into powerpoint template) but just to give you a flavor of where we have been and have used in the past.

Target Market(s)

Institutional investors, asset managers, large fund institutions

Industry/Entity Type

Financial

Requirements
Must have
• Our logo
Traditional size
Nice to have
• unique use of logo, unique material, die cut, etc
Crisp, clean look
Use of both sides of card in a creative manner

```html
<!DOCTYPE html>
<html lang="en">
<head>
<meta charset="utf-8">
<title>Bramble Harbor Business Cards</title>
<link rel="stylesheet" href="https://fonts.googleapis.com/css2?family=Roboto:wght@400;700&display=swap">
<style>
  :root {
    --backdrop: #3a3939;
    --card-white: #ffffff;
    --card-mist: #f2f2f2;
    --card-edge: #d6d6d6;
    --ink-grey: #666769;
    --ink-soft: #555555;
    --accent-orange: #f39a2b;
    --rule-grey: #8a8a8a;
  }
  * { margin: 0; padding: 0; box-sizing: border-box; }
  html, body {
    width: 1200px;
    height: 780px;
    overflow: hidden;
    background: var(--backdrop);
    font-family: "Roboto", Arial, sans-serif;
  }
  .stage { position: relative; width: 1200px; height: 780px; }

  .card {
    position: absolute;
    border-radius: 62px 0 62px 0;
    overflow: hidden;
  }
  .card--white { background: var(--card-white); }
  .card--mist { background: var(--card-mist); border: 1px solid var(--card-edge); }

  .card--front-a { left: 66px; top: 74px; width: 496px; height: 284px; }
  .card--back-a  { left: 594px; top: 92px; width: 497px; height: 283px; }
  .card--front-b { left: 66px; top: 408px; width: 504px; height: 281px; }
  .card--back-b  { left: 603px; top: 408px; width: 495px; height: 284px; }

  .wordmark {
    position: absolute;
    display: flex;
    align-items: center;
    gap: 8px;
    color: var(--ink-grey);
    font-weight: 700;
    line-height: 1;
  }
  .wordmark__dot {
    flex: none;
    border-radius: 50%;
    background: var(--accent-orange);
  }
  .wordmark__name { display: flex; flex-direction: column; }

  .wordmark--small { left: 16px; font-size: 19px; letter-spacing: 0.5px; }
  .wordmark--small .wordmark__dot { width: 14px; height: 14px; }
  .card--front-a .wordmark--small { top: 116px; }
  .card--front-b .wordmark--small { top: 116px; }

  .wordmark--large { left: 56px; top: 84px; font-size: 46px; letter-spacing: 1px; gap: 16px; }
  .wordmark--large .wordmark__name span + span { margin-top: 8px; }
  .wordmark--large .wordmark__dot { width: 34px; height: 34px; }

  .divider {
    position: absolute;
    left: 216px;
    top: 52px;
    width: 1px;
    height: 196px;
    background: var(--rule-grey);
  }
  .card--front-b .divider { left: 192px; top: 50px; height: 194px; }

  .contact {
    position: absolute;
    left: 235px;
    font-size: 11.5px;
    line-height: 18px;
    color: var(--ink-soft);
  }
  .card--front-b .contact { left: 211px; }
  .contact--address { top: 62px; }
  .contact--online { top: 182px; }
</style>
</head>
<body>
<main class="stage">

  <section class="card card--white card--front-a">
    <div class="wordmark wordmark--small">
      <span class="wordmark__name">BRAMBLE HARBOR</span>
    </div>
    <div class="divider"></div>
    <address class="contact contact--address" style="font-style:normal">
      Bramble Harbor, Inc<br>
      2189 Fernhollow Ridge Road<br>
      Suite 418<br>
      Cedar Mills, CA 90412<br>
      P 555.204.7781
    </address>
    <p class="contact contact--online">
      Marketing@BrambleHarbor.com<br>
      www.brambleharbor.com
    </p>
  </section>

  <section class="card card--white card--back-a">
    <div class="wordmark wordmark--large">
      <span class="wordmark__name"><span>BRAMBLE</span><span>HARBOR</span></span>
      <span class="wordmark__dot"></span>
    </div>
  </section>

  <section class="card card--mist card--front-b">
    <div class="wordmark wordmark--small">
      <span class="wordmark__name">BRAMBLE HARBOR</span>
    </div>
    <div class="divider"></div>
    <address class="contact contact--address" style="font-style:normal">
      Bramble Harbor, Inc<br>
      2189 Fernhollow Ridge Road<br>
      Suite 418<br>
      Cedar Mills, CA 90412<br>
      P 555.204.7781
    </address>
    <p class="contact contact--online">
      Marketing@BrambleHarbor.com<br>
      www.brambleharbor.com
    </p>
  </section>

  <section class="card card--mist card--back-b">
    <div class="wordmark wordmark--large">
      <span class="wordmark__name"><span>BRAMBLE</span><span>HARBOR</span></span>
      <span class="wordmark__dot"></span>
    </div>
  </section>

</main>
</body>
</html>
```